Broschüre für gemeinnütziges Unternehmen in den Bereichen Kunst, Kultur, Genuss und Heimatpflege
Guten Morgen Tilda am Mühlbach, lieben Dank für die schöne, flexible und rasche Arbeit! Top Kontakt! Habe den Erhalt der Daten eben bestätigt. Viele Grüße Harald Wolting
Zielgruppe
Wir kümmern uns als gemeinnützige GmbH in der Stadt Lindenhain um alles, was mit Kunst, Kultur, Genuss und Heimatpflege zu tun hat. Dafür erstellen wir immer zum Jahresende (Ende Oktober, Anfang November) eine Broschüre mit unserem Programm für das Folgejahr. Unsere Zielgruppe sind Bürgerinnen und Bürger aus dem ganzen Kreisgebiet und darüber hinaus, Altersstruktur 30plus. Der neue Look der Broschüre sollte hochwertig und modern sein.
Aufgabenstellung
Die Broschüre hat eine Klammerheftung und wird ca. 64 Seiten umfassen.
Format: 14,8 x 14,8 cm
In der Anlage an diese Anfrage befinden sich Fotos von Musterseiten, wobei 'Titelseite' die aktuelle Titelseite zeigt, 'Foto 1' eine bisherige Innenseite zeigt, 'Seite 2' und 'Seite 3/4' zeigen Musterseiten, die verdeutlichen sollen, in welche Moderene und reduzierte Richtung es gehen soll. 'Foto Übersicht' zeigt eine chronologische Übersicht. Die Broschüre soll also einen moderneren Look bekommen, gerne auch mal mit einer Doppelseite. Die Musterseiten 2 und 3/4 sind allerdings aus einer Broschüre einer Nachbarkommune, unser Heft sollte sich also davon unterscheiden.
Wichtig sind immer pro Innenseite (oder Innen-Doppelseite): Ein Foto, Titel (z.B. 'Malvina', Genre 'Live-Musik' oder 'Musik und Songnächte', Eckdaten (Datum, Uhrzeit, Location, weitere Infos), Text.
Uns wäre mit einer schön gestalteten Titelseite, sowie schön gestalteten Muster-Innenseiten (je eine Einzelseite, eine Doppelseite, eine Seite mit tabellarischer Übersicht) sehr geholfen. Wir würden dann mit der Vorlage arbeiten und die anderen Seiten 'bauen'. Wäre das ein gangbarer Weg?
Für die Titelseite kann sehr gerne Stockmaterial verwendet werden, für den Innenteil stellen wir die Fotos.
Vielleicht können Musterseiten zu 'Malvina' ('Foto 1') gestaltet werden? Das passenden Foto hängt an, es kann mit Blindtext gearbeitet werden.
Ich freue mich über ein rasches Angebot.
Ihr
Harald Wolting

```html
<!DOCTYPE html>
<html lang="de">
<head>
<meta charset="utf-8">
<title>Eventmagazin Lindenhain 2024 – Umschlag</title>
<link href="https://fonts.googleapis.com/css2?family=Fira+Sans:ital,wght@0,400;0,500;0,600;1,500&family=Fira+Sans+Condensed:wght@500&display=swap" rel="stylesheet">
<style>
  :root {
    --night: #000000;
    --night-haze: #14142e;
    --white: #ffffff;
    --teal: #1a7f94;
    --teal-text: #1f8aa0;
    --stage-blue: #2f7fd0;
    --stage-violet: #5a36a8;
    --crowd-deep: #1c1240;
  }
  * { margin: 0; padding: 0; box-sizing: border-box; }
  html, body { width: 1200px; height: 600px; overflow: hidden; background: var(--night); }
  .spread { position: relative; width: 1200px; height: 600px; display: flex; font-family: "Fira Sans", sans-serif; color: var(--white); }

  .back-cover { position: relative; width: 600px; height: 600px; background: var(--night); }
  .back-cover .haze-photo {
    position: absolute; left: 0; top: 0; width: 432px; height: 600px;
    background: linear-gradient(180deg, #05050e 0%, var(--night-haze) 45%, #0c0c22 75%, #05050c 100%);
  }
  .back-cover .brand {
    position: absolute; left: 0; width: 600px; top: 236px; text-align: center;
    display: flex; justify-content: center; align-items: center; gap: 12px;
    font-size: 34px; font-weight: 600; letter-spacing: 0.02em;
  }
  .brand .brand-square { width: 22px; height: 22px; background: var(--white); display: inline-block; }
  .back-cover .web {
    position: absolute; left: 0; width: 600px; top: 359px; text-align: center;
    font-family: "Fira Sans Condensed", sans-serif; font-weight: 500; font-size: 13px;
  }
  .back-cover .welcome {
    position: absolute; left: 0; width: 600px; top: 539px; text-align: center;
    font-size: 14.5px; font-weight: 500; letter-spacing: 0.01em;
  }

  .front-cover { position: relative; width: 600px; height: 600px; overflow: hidden; }
  .front-cover .concert-photo {
    position: absolute; inset: 0;
    background:
      radial-gradient(ellipse 60% 40% at 70% 8%, rgba(120,200,240,0.85), transparent 70%),
      radial-gradient(ellipse 70% 50% at 80% 35%, rgba(190,120,220,0.55), transparent 70%),
      linear-gradient(160deg, var(--stage-blue) 0%, var(--stage-violet) 45%, var(--crowd-deep) 100%);
  }
  .front-cover .brand {
    position: absolute; left: 44px; top: 82px; display: flex; align-items: center; gap: 8px;
    font-size: 22px; font-weight: 600;
  }
  .front-cover .brand .brand-square { width: 14px; height: 14px; }
  .front-cover .web {
    position: absolute; left: 44px; top: 140px;
    font-family: "Fira Sans Condensed", sans-serif; font-weight: 500; font-size: 12.5px;
  }
  .front-cover .tagline {
    position: absolute; left: 44px; top: 257px;
    font-size: 20px; font-style: italic; font-weight: 500; color: var(--teal-text); white-space: nowrap;
  }
  .front-cover .title {
    position: absolute; left: 43px; top: 282px; font-weight: 500; line-height: 1;
    text-transform: uppercase;
  }
  .title .title-line { display: block; font-size: 38.5px; letter-spacing: 0.09em; line-height: 36px; }
  .title .title-year { display: block; font-size: 66px; letter-spacing: 0.03em; line-height: 62px; margin-top: 2px; }
  .front-cover .accent-bar { position: absolute; left: 645px; }
  .accent-bar { position: absolute; left: 45px; top: 437px; width: 69px; height: 10px; background: var(--teal); }
</style>
</head>
<body>
<main class="spread">
  <section class="back-cover">
    <div class="haze-photo" role="img" aria-label="Dunkles Foto mit Bühnennebel in Nachtblau"></div>
    <div class="brand"><span class="brand-square"></span>Lindenhain</div>
    <p class="web">www.lindenhain-erleben.de</p>
    <p class="welcome">WIR FREUEN UNS AUF IHREN BESUCH!</p>
  </section>

  <section class="front-cover">
    <div class="concert-photo" role="img" aria-label="Konzertfoto: Publikum mit erhobenen Händen vor blau und violett leuchtender Bühne"></div>
    <div class="brand"><span class="brand-square"></span>Lindenhain</div>
    <p class="web">www.lindenhain-erleben.de</p>
    <p class="tagline">KUNST / KULTUR / GENUSS / GLÜCK</p>
    <h1 class="title">
      <span class="title-line">Eventmagazin</span>
      <span class="title-line">Lindenhain</span>
      <span class="title-year">2024</span>
    </h1>
    <div class="accent-bar"></div>
  </section>
</main>
</body>
</html>
```